velunique hair oil

Its an ayurvedic hair oil of 100 ml bottle. We need a design for the label. along with the wordings, some punch line too in the label. Mettalic silver bottle with black cap. Round bottle with height of 10 cm and width of 7 cm. The metallic silver colour bottle can be changed if some other nice colour combination is worked out

Target Market(s)

Retail, any one with a hair fall problem can be our target customer.. This ayurvedic hair oil is a miracle off sorts. With just one bottle hair fall totally stops and fresh hair grows.

Industry/Entity Type

Hair

Requirements
Must have
• HAVE WORDS 100% AYURVEDIC HAIR OIL IN A CIRCLE

MUST NOTE THAT THE BOTTLE IS ROUND
Nice to have
• Its for both men and women. Bottle is round in shape and hence the wording should be accordingly put
Should not have
• RED COLOUR.

```html
<!DOCTYPE html>
<html lang="en">
<head>
<meta charset="utf-8">
<title>Velunique Ayurvedic Hair Oil Label</title>
<link rel="stylesheet" href="https://fonts.googleapis.com/css2?family=Comfortaa:wght@400&display=swap">
<style>
  :root {
    --leaf-green: #8cc63f;
    --pattern-grey: #a3a3a3;
    --panel-mint: rgba(222, 240, 196, 0.86);
    --ink: #3b3b3b;
  }
  html, body {
    margin: 0;
    padding: 0;
    width: 1200px;
    height: 2395px;
    overflow: hidden;
    background: #ffffff;
  }
  .label {
    position: relative;
    width: 1200px;
    height: 2395px;
    overflow: hidden;
    font-family: "Comfortaa", sans-serif;
    font-weight: 400;
    color: var(--ink);
  }
  .label__pattern {
    position: absolute;
    inset: 0;
    background:
      radial-gradient(circle at 20% 15%, var(--pattern-grey) 0 12%, transparent 13%),
      radial-gradient(circle at 85% 40%, var(--pattern-grey) 0 10%, transparent 11%),
      radial-gradient(circle at 15% 75%, var(--pattern-grey) 0 11%, transparent 12%),
      radial-gradient(circle at 80% 90%, var(--pattern-grey) 0 9%, transparent 10%),
      linear-gradient(160deg, #93cc45 0%, var(--leaf-green) 50%, #7fbb34 100%);
  }
  .label__panel {
    position: absolute;
    left: 43px;
    top: 48px;
    width: 1114px;
    height: 2294px;
    border-radius: 48px;
    background: var(--panel-mint);
  }
  .brand-name {
    position: absolute;
    top: 235px;
    left: 0;
    width: 100%;
    margin: 0;
    text-align: center;
    font-weight: 400;
    font-size: 150px;
    line-height: 1;
  }
  .audience {
    position: absolute;
    top: 445px;
    left: 0;
    width: 100%;
    margin: 0;
    text-align: center;
    font-size: 68px;
    line-height: 1;
  }
  .claim-circle {
    position: absolute;
    left: 348px;
    top: 924px;
    width: 496px;
    height: 496px;
    border: 6px solid var(--ink);
    border-radius: 50%;
    display: flex;
    flex-direction: column;
    align-items: center;
    justify-content: center;
    text-align: center;
  }
  .claim-circle span {
    display: block;
    font-size: 62px;
    line-height: 1.25;
  }
  .claim-circle .claim-circle__figure {
    font-size: 150px;
    line-height: 1.1;
  }
  .claim {
    position: absolute;
    top: 1580px;
    left: 0;
    width: 100%;
    margin: 0;
    text-align: center;
    font-size: 70px;
    line-height: 99px;
  }
  .volume {
    position: absolute;
    top: 2225px;
    left: 0;
    width: 100%;
    margin: 0;
    text-align: center;
    font-size: 62px;
    line-height: 1;
  }
</style>
</head>
<body>
<main class="label">
  <div class="label__pattern" role="img" aria-label="Green and grey paisley and mandala pattern covering the label"></div>
  <div class="label__panel"></div>

  <h1 class="brand-name">Velunique</h1>
  <p class="audience">For Men and Women</p>

  <div class="claim-circle">
    <span>AYURVEDIC</span>
    <span class="claim-circle__figure">100%</span>
    <span>HAIR OIL</span>
  </div>

  <p class="claim">This ayurvedic hair oil<br>is a miracle off sorts.<br>With just one bottle<br>hair fall totally stops<br>and fresh hair grows.</p>

  <p class="volume">100ml</p>
</main>
</body>
</html>
```